Nest Sack new product

Re-usable baby food pouch. Need artwork for new product.
Primarily green, some clear space (1/3 - 1/2 clear) so you can see through to whats inside.

To be fresh, organic looking and to appeal to kids and families.

Portrait style 18xm long, 11cm wide.

Need a front and back version (both this size)

please see similar products on www.brightmorsels.example and www.tinyfernsack.example

Target Market(s)

Families, kids product

Industry/Entity Type

Baby

Colors
9ccb3b

Requirements
Must have
• Clear space as described.
Under Logo
"reusable food pouch"
BPA Free- dishwasher safe- freezer safe

On back
Logo
Tick boxes
Freezer safe
dishwasher safe
BPA Phthalate & PVC Free
160 mls
DO NOT MICROWAVE

"to warm contents simply place filled pouch in a bowl of hot water" Keep the cap out of reach of children 3 and under.

www.nestsacks.example.au

```html
<!DOCTYPE html>
<html lang="en">
<head>
<meta charset="utf-8">
<title>Nest Sack – Reusable Food Pouch</title>
<link href="https://fonts.googleapis.com/css2?family=Fredoka:wght@400;500;600&display=swap" rel="stylesheet">
<style>
  :root {
    --brand-green: #9ccb3b;
    --pouch-green: #8cc63f;
    --window-green: #cfe7a4;
    --panel-teal-light: #56b4ae;
    --info-blue: #4ab3d8;
    --cap-clear: #eef2f2;
    --cap-edge: #c9d1d1;
    --bg-center: #f7f7f7;
    --bg-edge: #d6d6d6;
    --tagline-grey: #bfc5bf;
    --white: #ffffff;
    --url-tint: #e3f2cc;
  }
  html, body {
    margin: 0;
    padding: 0;
    width: 1200px;
    height: 987px;
    overflow: hidden;
  }
  body {
    background: radial-gradient(ellipse at 50% 35%, var(--bg-center) 0%, #ececec 50%, var(--bg-edge) 100%);
    font-family: "Fredoka", "Trebuchet MS", sans-serif;
  }
  .board { display: block; width: 1200px; height: 987px; }
  .brand-name { fill: var(--brand-green); font-weight: 600; }
  .brand-tagline { fill: var(--tagline-grey); font-weight: 500; letter-spacing: 1px; }
  .pouch-body { fill: var(--pouch-green); }
  .pouch-pattern { fill: url(#leafTone); }
  .pouch-window { fill: var(--window-green); }
  .stitch { fill: none; stroke: var(--white); stroke-width: 1.6; stroke-dasharray: 5 4; }
  .spout-neck { fill: var(--cap-clear); stroke: var(--cap-edge); stroke-width: 1; }
  .spout-cap { fill: var(--cap-clear); stroke: var(--cap-edge); stroke-width: 1.2; }
  .pouch-name { fill: var(--white); font-weight: 600; }
  .pouch-mark { fill: var(--white); }
  .pouch-tagline { fill: var(--white); font-weight: 500; letter-spacing: 0.4px; }
  .claims-bar { fill: var(--panel-teal-light); }
  .claims-text { fill: var(--white); font-weight: 600; }
  .info-panel { fill: url(#panelTone); }
  .info-warm { fill: var(--info-blue); }
  .info-rule { stroke: var(--white); stroke-width: 0.8; }
  .info-text { fill: var(--white); font-weight: 500; }
  .icon-fill { fill: #e6ecec; stroke: #b9c4c4; stroke-width: 0.8; }
  .icon-detail { stroke: #9aa6a6; stroke-width: 1.2; fill: none; }
  .tick-box { fill: none; stroke: var(--white); stroke-width: 0.9; }
  .tick-mark { fill: none; stroke: var(--white); stroke-width: 1.2; stroke-linecap: round; stroke-linejoin: round; }
  .pouch-url { fill: var(--url-tint); font-weight: 600; letter-spacing: 0.4px; }
</style>
</head>
<body>
<svg class="board" viewBox="0 0 900 740" xmlns="http://www.w3.org/2000/svg" aria-labelledby="boardTitle">
  <title id="boardTitle">Nest Sack reusable food pouch, front and back</title>
  <defs>
    <linearGradient id="leafTone" x1="0" y1="0" x2="1" y2="1">
      <stop offset="0" stop-color="#94cc45"/>
      <stop offset="0.5" stop-color="#7fbd36"/>
      <stop offset="1" stop-color="#8ec63f"/>
    </linearGradient>
    <linearGradient id="panelTone" x1="0" y1="0" x2="0" y2="1">
      <stop offset="0" stop-color="#5aa795"/>
      <stop offset="1" stop-color="#3c9f9c"/>
    </linearGradient>
  </defs>

  <!-- Brand header -->
  <g class="brand-header">
    <circle cx="350" cy="108" r="42" fill="var(--brand-green)"/>
    <text class="brand-name" x="410" y="104" font-size="58">Nest</text>
    <text class="brand-name" x="410" y="160" font-size="58">Sack</text>
    <text class="brand-tagline" x="450" y="201" font-size="17" text-anchor="middle">REUSABLE FOOD POUCH</text>
  </g>

  <!-- Front of pouch -->
  <g class="pouch pouch-front">
    <path class="pouch-body pouch-pattern" role="img" aria-label="Soft leaf and fruit pattern in layered greens"
      d="M115,292 Q115,282 128,280 L183,272 L185,252 L300,246 L306,258 L345,300 L385,312 Q395,316 395,328 L395,605 Q395,620 380,620 L130,620 Q115,620 115,605 Z"/>
    <rect class="pouch-window" x="140" y="305" width="195" height="188" rx="18"/>
    <path class="stitch" d="M132,322 Q132,304 150,302 L195,298 L200,276 L292,272 L302,290 L322,298 Q342,304 342,324 L342,478 Q342,496 325,508 Q305,528 292,544 Q284,552 266,552 L152,552 Q132,552 132,532 Z"/>
    <circle class="pouch-mark" cx="190" cy="520" r="11"/>
    <text class="pouch-name" x="206" y="516" font-size="21">Nest</text>
    <text class="pouch-name" x="206" y="538" font-size="21">Sack</text>
    <text class="pouch-tagline" x="236" y="566" font-size="11" text-anchor="middle">REUSABLE FOOD POUCH</text>
    <rect class="claims-bar" x="140" y="577" width="192" height="17" rx="3"/>
    <text class="claims-text" x="236" y="588.5" font-size="7" text-anchor="middle">BPA FREE  •  DISHWASHER SAFE  •  FREEZER SAFE</text>
    <rect class="spout-neck" x="342" y="334" width="18" height="30" rx="3"/>
    <rect class="spout-cap" x="356" y="310" width="52" height="72" rx="12"/>
  </g>

  <!-- Back of pouch -->
  <g class="pouch pouch-back">
    <path class="pouch-body"
      d="M553,300 Q553,288 566,286 L620,278 L645,256 L650,248 L755,245 L760,258 L778,268 Q790,272 790,285 L790,605 Q790,620 775,620 L568,620 Q553,620 553,605 Z"/>
    <path class="stitch" d="M572,312 Q572,298 585,296 L625,288 L655,266 L740,266 L752,280 L765,284 Q775,288 775,302 L775,586 Q775,596 765,596 L582,596 Q572,596 572,586 Z"/>
    <rect class="spout-neck" x="542" y="334" width="18" height="30" rx="3"/>
    <rect class="spout-cap" x="510" y="312" width="46" height="72" rx="12"/>

    <circle class="pouch-mark" cx="632" cy="340" r="13"/>
    <text class="pouch-name" x="652" y="336" font-size="21">Nest</text>
    <text class="pouch-name" x="652" y="358" font-size="21">Sack</text>

    <rect class="info-panel" x="598" y="377" width="155" height="207"/>

    <g class="icon icon-freezer">
      <rect class="icon-fill" x="619" y="384" width="28" height="42" rx="2"/>
      <line x1="619" y1="399" x2="647" y2="399" stroke="#b9c4c4" stroke-width="0.8"/>
      <line class="icon-detail" x1="623" y1="389" x2="623" y2="395"/>
      <line class="icon-detail" x1="623" y1="404" x2="623" y2="414"/>
    </g>
    <g class="icon icon-dishwasher">
      <rect class="icon-fill" x="684" y="388" width="34" height="38" rx="2"/>
      <line x1="684" y1="396" x2="718" y2="396" stroke="#b9c4c4" stroke-width="0.8"/>
      <rect x="689" y="400" width="24" height="22" fill="none" stroke="#b9c4c4" stroke-width="0.8"/>
      <line class="icon-detail" x1="695" y1="404" x2="707" y2="404"/>
    </g>

    <g class="checklist">
      <rect class="tick-box" x="614" y="432" width="6" height="6"/>
      <path class="tick-mark" d="M615,434 L617.5,437 L622,430"/>
      <text class="info-text" x="624" y="438" font-size="7.5">Freezer</text>
      <text class="info-text" x="628" y="447" font-size="7.5">safe</text>

      <rect class="tick-box" x="678" y="432" width="6" height="6"/>
      <path class="tick-mark" d="M679,434 L681.5,437 L686,430"/>
      <text class="info-text" x="688" y="438" font-size="7.5">Dishwasher</text>
      <text class="info-text" x="696" y="447" font-size="7.5">safe</text>

      <rect class="tick-box" x="614" y="458" width="6" height="6"/>
      <path class="tick-mark" d="M615,460 L617.5,463 L622,456"/>
      <text class="info-text" x="624" y="464" font-size="7.5">BPA Phthalate &amp; PVC free</text>
    </g>

    <rect class="info-warm" x="600" y="478" width="151" height="70"/>
    <text class="info-text" x="675.5" y="490" font-size="6.8" text-anchor="middle">"To warm contents simply place</text>
    <text class="info-text" x="675.5" y="499" font-size="6.8" text-anchor="middle">filled pouch in a bowl of hot water"</text>
    <line class="info-rule" x1="604" y1="506" x2="747" y2="506"/>
    <text class="info-text" x="675.5" y="519" font-size="6.8" text-anchor="middle">Keep the cap out of reach of</text>
    <text class="info-text" x="675.5" y="529" font-size="6.8" text-anchor="middle">children 3 and under.</text>

    <text class="info-text" x="608" y="569" font-size="7.5" font-weight="600">160 mls</text>
    <text class="info-text" x="658" y="569" font-size="7">DO NOT MICROWAVE</text>

    <text class="pouch-url" x="673" y="609" font-size="7.5" text-anchor="middle">www.nestsacks.example.au</text>
  </g>
</svg>
</body>
</html>
```